Creative Challenge - Disruptive Digital Construction Business needs an Application Design

We need an application design (4 screens).
The app will offer easy-to-use an interactive course to illustrate the latest technology to construction professionals. Kindly find the attachments.
Updates

I have just posted the contest and the deadline is tomorrow!! Please give me my original 7 days back.

Need extra days to review

Target Market(s)

Construction professionals, aged from 22 to 36, who want to learn new disruptive technologies in construction.

Colors
e667a6
b868aa
33a6d7

Requirements
Must have
• The name of the app, Velmiro, stands for “Virtual Engineering Leaders”. The user is a Velmiro, who would transform the digital construction industry. We want a design that gives that feel to the users.

```html
<!DOCTYPE html>
<html lang="en">
<head>
<meta charset="utf-8">
<title>Velmiro – App Screens</title>
<link href="https://fonts.googleapis.com/css2?family=Poppins:wght@400;500;600&display=swap" rel="stylesheet">
<style>
:root{
  --pink:#e667a6;--blue:#33a6d7;--purple:#a94fc4;--magenta:#d2489a;
  --ink:#2b2b33;--muted:#9a9ca3;--field:#ffffff;--screen:#f6f6f8;
  --skyline:#c9cbd0;--bg:#eceef1;
}
*{box-sizing:border-box;margin:0;padding:0}
html,body{width:1200px;height:534px;overflow:hidden}
body{background:var(--bg);font-family:'Poppins',sans-serif;color:var(--ink);position:relative}
.set{position:absolute;width:556px;height:219px}
.t1{left:26px;top:23px;--p:var(--pink);--cust:var(--blue);--list:var(--pink);--fav:var(--blue);--play:var(--blue);--tog:var(--blue);--btn:var(--blue);--btn2:var(--blue)}
.t2{left:609px;top:23px;--p:var(--blue);--cust:var(--pink);--list:var(--blue);--fav:var(--pink);--play:var(--pink);--tog:var(--pink);--btn:var(--pink);--btn2:var(--pink)}
.t3{left:26px;top:274px;--p:var(--purple);--cust:var(--purple);--list:var(--purple);--fav:transparent;--play:#111;--tog:var(--purple);--btn:var(--purple);--btn2:var(--purple)}
.t4{left:611px;top:274px;--p:var(--magenta);--cust:var(--blue);--list:var(--magenta);--fav:transparent;--play:var(--blue);--tog:var(--blue);--btn:var(--blue);--btn2:var(--blue)}
.screen{position:absolute;top:27px;width:75px;height:165px;background:var(--screen);border-radius:8px;overflow:hidden;box-shadow:0 2px 6px rgba(0,0,0,.12)}
.s1{left:43px}.s2{left:142px}.s3{left:240px}.s4{left:339px}.s5{left:438px}
.abs{position:absolute}
.status{position:absolute;top:5px;left:0;right:0;text-align:center;font-size:3.6px;font-weight:500}
.status.light{color:#fff}
.header{position:absolute;left:0;top:0;width:75px;background:var(--p)}
.wave{position:absolute;left:0;width:75px}
.wave path{fill:var(--p)}
.head-text{position:absolute;left:4px;right:4px;text-align:center;color:#fff;font-size:3.1px;line-height:1.3}
.title{position:absolute;left:0;right:0;text-align:center;font-size:4px;font-weight:600}
.brand{position:absolute;left:0;right:0;top:64px;text-align:center;font-size:5.2px;font-weight:600}
.field{position:absolute;left:10px;width:55px;height:6px;background:var(--field);border-radius:3px;font-size:2.1px;color:var(--muted);padding-left:3px;line-height:6px;box-shadow:0 0 2px rgba(0,0,0,.06)}
.field .dot{position:absolute;right:2px;top:1.5px;width:3px;height:3px;border-radius:50%;background:var(--p)}
.btn{position:absolute;left:10px;width:55px;height:7px;border-radius:4px;background:var(--btn);color:#fff;font-size:2.6px;text-align:center;line-height:7px}
.small{position:absolute;left:0;right:0;text-align:center;font-size:1.9px;color:var(--muted)}
.small b{color:var(--ink);font-weight:500;text-decoration:underline}
.skyline{position:absolute;left:0;bottom:0;width:75px;height:30px;background:linear-gradient(180deg,rgba(201,203,208,0),var(--skyline) 60%)}
.bar{position:absolute;left:10px;width:55px;height:6px;border-radius:3px;font-size:2px;color:#fff;padding-left:3px;line-height:6px}
.bar::after{content:"›";position:absolute;right:3px;top:0}
.cust{background:var(--cust)}
.list{background:var(--list)}
.opts{position:absolute;left:10px;top:41px;width:55px;height:35px;background:#efeff2;border-radius:2px}
.opt{position:absolute;left:3px;font-size:1.7px;color:var(--muted);padding-left:7px;width:50px;line-height:1.3}
.opt::before{content:"";position:absolute;left:0;top:0;width:5px;height:2.4px;border-radius:2px;background:var(--tog)}
.menu{position:absolute;left:0;top:0;width:61px;height:153px;background:var(--p);border-bottom-right-radius:6px;overflow:hidden}
.avatar{position:absolute;left:21px;top:13px;width:19px;height:19px;border-radius:50%;background:radial-gradient(circle at 50% 40%,#e7e2de,#9a9590);border:1px solid #fff}
.name{position:absolute;left:0;right:0;top:36px;text-align:center;color:#fff;font-size:3.6px;font-weight:500}
.role{position:absolute;left:0;right:0;top:41px;text-align:center;color:#fff;font-size:1.8px;opacity:.9}
.item{position:absolute;left:0;width:55px;height:8px;color:#fff;font-size:2.3px;line-height:8px;padding-left:15px}
.item.fav{background:var(--fav);border-radius:0 4px 4px 0}
.item i{position:absolute;left:9px;top:2.5px;width:3px;height:3px;border-radius:.5px;background:#fff}
.menu .skyline{height:32px;bottom:0;width:61px;background:linear-gradient(180deg,rgba(0,0,0,0),rgba(0,0,0,.18))}
.side-status{position:absolute;right:3px;top:5px;font-size:2.6px;color:var(--ink)}
.check{position:absolute;left:12px;font-size:1.8px;color:var(--muted);padding-left:5px}
.check svg{position:absolute;left:0;top:-.3px}
.check path{stroke:var(--p);fill:none;stroke-width:1}
.video{position:absolute;left:6px;top:67px;width:63px;height:47px;border-radius:4px;background:linear-gradient(135deg,color-mix(in srgb,var(--p) 35%,#fff),color-mix(in srgb,var(--p) 80%,#234))}
.playc{position:absolute;left:25px;top:17px;width:13px;height:13px;border-radius:50%;background:#fff}
.player{position:absolute;left:13px;top:119px;width:49px;height:9px;border-radius:5px;background:var(--play)}
.slider{position:absolute;left:12px;top:136px;width:51px;height:.6px;background:#dcdce0}
.slider span{position:absolute;left:12px;top:-1px;width:2.4px;height:2.4px;border-radius:50%;background:var(--play)}
.t3 .slider span{background:var(--purple)}
.cap{position:absolute;left:0;right:0;top:142px;text-align:center;font-size:3.6px;font-weight:600}
.lorem{position:absolute;left:10px;right:10px;top:149px;text-align:center;font-size:1.7px;color:var(--muted);line-height:1.4}
</style>
</head>
<body>

<!-- shared template repeated per colour theme -->
<section class="set t1">
  <div class="screen s1">
    <div class="header" style="height:44px"></div>
    <svg class="wave" style="top:43px" width="75" height="12" viewBox="0 0 75 12" preserveAspectRatio="none"><path d="M0 0H75V2C60 2 52 12 35 10S10 3 0 10Z"/></svg>
    <div class="status light">22:14</div>
    <div class="head-text" style="top:22px">Welcome to<br>Virtual Engineering Leaders</div>
    <div class="brand">Velmiro</div>
    <div class="field" style="top:82px">Email</div>
    <div class="field" style="top:94px">Password</div>
    <div class="btn" style="top:109px">Login</div>
    <div class="small" style="top:124px">Sign up &nbsp;OR&nbsp; Sign up via <b>Crewnet</b></div>
    <div class="skyline" role="img" aria-label="Construction site skyline illustration"></div>
  </div>
  <div class="screen s2">
    <div class="status">22:14</div>
    <div class="title" style="top:21px">Create an Account</div>
    <div class="field" style="top:35px">Name</div>
    <div class="field" style="top:47px">Email</div>
    <div class="field" style="top:59px">Mobile No.</div>
    <div class="field" style="top:71px">Password</div>
    <div class="field" style="top:83px">Gender<span class="dot"></span></div>
    <div class="field" style="top:95px">Country of Residence<span class="dot"></span></div>
    <div class="field" style="top:107px">Company</div>
    <div class="field" style="top:119px">Title</div>
    <div class="field" style="top:131px">Year of Experience<span class="dot"></span></div>
    <div class="btn" style="top:146px;background:var(--btn2)">Sign Up</div>
  </div>
  <div class="screen s3">
    <div class="status">22:14</div>
    <div class="title" style="top:21px">Your Journey Starts Here</div>
    <div class="bar cust" style="top:33px">Customise your Journey</div>
    <div class="opts">
      <div class="opt" style="top:3px">Show All</div>
      <div class="opt" style="top:8px">I am the client (Appointing Party)</div>
      <div class="opt" style="top:14px">I am the lead consultant / lead contractor (Appointed Party)</div>
      <div class="opt" style="top:25px">I am the consultant / subcontractor / supplier (Appointed Party)</div>
    </div>
    <div class="bar list" style="top:86px">How to start BIM?</div>
    <div class="bar list" style="top:95px">Important ISO19650 principles to know</div>
    <div class="bar list" style="top:104px">Information Management Processes &amp; Act…</div>
    <div class="bar list" style="top:113px">Documents/Resources You Need to Develop</div>
    <div class="bar list" style="top:122px">Other Resources</div>
    <div class="skyline" role="img" aria-label="Crane and building site illustration"></div>
  </div>
  <div class="screen s4">
    <div class="side-status">▮▮</div>
    <div class="menu">
      <div class="avatar" role="img" aria-label="Profile photo of the user"></div>
      <div class="name">Name Here</div>
      <div class="role">Professionals</div>
      <div class="item fav" style="top:51px"><i></i>My favorite</div>
      <div class="item" style="top:62px"><i></i>Search</div>
      <div class="item" style="top:73px"><i></i>About the app</div>
      <div class="item" style="top:84px"><i></i>About the authors</div>
      <div class="item" style="top:95px"><i></i>Log out</div>
      <div class="skyline" role="img" aria-label="Workers and crane on a building site illustration"></div>
    </div>
  </div>
  <div class="screen s5">
    <div class="header" style="height:30px"></div>
    <svg class="wave" style="top:29px" width="75" height="12" viewBox="0 0 75 12" preserveAspectRatio="none"><path d="M0 0H75V4C60 12 40 2 20 8S5 9 0 6Z"/></svg>
    <div class="status light">22:14</div>
    <div class="head-text" style="top:13px">Nominate individuals to undertake the information management function</div>
    <div class="check" style="top:48px"><svg width="3" height="3" viewBox="0 0 3 3"><path d="M.3 1.5L1.2 2.5 2.8.3"/></svg>Appointment level</div>
    <div class="check" style="top:53px"><svg width="3" height="3" viewBox="0 0 3 3"><path d="M.3 1.5L1.2 2.5 2.8.3"/></svg>Information Procurement Stage</div>
    <div class="check" style="top:58px"><svg width="3" height="3" viewBox="0 0 3 3"><path d="M.3 1.5L1.2 2.5 2.8.3"/></svg>Actor: The Lead Appointed Party</div>
    <div class="video" role="img" aria-label="Video still of engineers reviewing plans on site"><div class="playc"></div></div>
    <svg class="player" width="49" height="9" viewBox="0 0 49 9"><path fill="#fff" d="M12 4.5l3-2v4zM15 4.5l3-2v4zM23 2.5l4 2-4 2zM31 2.5l3 2-3 2zM34 2.5l3 2-3 2z"/></svg>
    <div class="slider"><span></span></div>
    <div class="cap">Illustration</div>
    <div class="lorem">Lorem ipsum is sometimes known as dummy text used in laying out print.</div>
  </div>
</section>

<section class="set t2">
  <div class="screen s1">
    <div class="header" style="height:44px"></div>
    <svg class="wave" style="top:43px" width="75" height="12" viewBox="0 0 75 12" preserveAspectRatio="none"><path d="M0 0H75V2C60 2 52 12 35 10S10 3 0 10Z"/></svg>
    <div class="status light">22:14</div>
    <div class="head-text" style="top:22px">Welcome to<br>Virtual Engineering Leaders</div>
    <div class="brand">Velmiro</div>
    <div class="field" style="top:82px">Email</div>
    <div class="field" style="top:94px">Password</div>
    <div class="btn" style="top:109px">Login</div>
    <div class="small" style="top:124px">Sign up &nbsp;OR&nbsp; Sign up via <b>Crewnet</b></div>
    <div class="skyline" role="img" aria-label="Construction site skyline illustration"></div>
  </div>
  <div class="screen s2">
    <div class="status">22:14</div>
    <div class="title" style="top:21px">Create an Account</div>
    <div class="field" style="top:35px">Name</div>
    <div class="field" style="top:47px">Email</div>
    <div class="field" style="top:59px">Mobile No.</div>
    <div class="field" style="top:71px">Password</div>
    <div class="field" style="top:83px">Gender</div>
    <div class="field" style="top:95px">Country of Residence</div>
    <div class="field" style="top:107px">Company</div>
    <div class="field" style="top:119px">Title</div>
    <div class="field" style="top:131px">Year of Experience</div>
    <div class="btn" style="top:146px;background:var(--btn2)">Sign Up</div>
  </div>
  <div class="screen s3">
    <div class="status">22:14</div>
    <div class="title" style="top:21px">Your Journey Starts Here</div>
    <div class="bar cust" style="top:33px">Customise your Journey</div>
    <div class="opts">
      <div class="opt" style="top:3px">Show All</div>
      <div class="opt" style="top:8px">I am the client (Appointing Party)</div>
      <div class="opt" style="top:14px">I am the lead consultant / lead contractor (Appointed Party)</div>
      <div class="opt" style="top:25px">I am the consultant / subcontractor / supplier (Appointed Party)</div>
    </div>
    <div class="bar list" style="top:86px">How to start BIM?</div>
    <div class="bar list" style="top:95px">Important ISO19650 principles to know</div>
    <div class="bar list" style="top:104px">Information Management Processes &amp; Act…</div>
    <div class="bar list" style="top:113px">Documents/Resources You Need to Develop</div>
    <div class="bar list" style="top:122px">Other Resources</div>
    <div class="skyline" role="img" aria-label="Crane and building site illustration"></div>
  </div>
  <div class="screen s4">
    <div class="side-status">▮▮</div>
    <div class="menu">
      <div class="avatar" role="img" aria-label="Profile photo of the user"></div>
      <div class="name">Name Here</div>
      <div class="role">Professionals</div>
      <div class="item fav" style="top:51px"><i></i>My favorite</div>
      <div class="item" style="top:62px"><i></i>Search</div>
      <div class="item" style="top:73px"><i></i>About the app</div>
      <div class="item" style="top:84px"><i></i>About the authors</div>
      <div class="item" style="top:95px"><i></i>Log out</div>
      <div class="skyline" role="img" aria-label="Workers and crane on a building site illustration"></div>
    </div>
  </div>
  <div class="screen s5">
    <div class="header" style="height:30px"></div>
    <svg class="wave" style="top:29px" width="75" height="12" viewBox="0 0 75 12" preserveAspectRatio="none"><path d="M0 0H75V4C60 12 40 2 20 8S5 9 0 6Z"/></svg>
    <div class="status light">22:14</div>
    <div class="head-text" style="top:13px">Nominate individuals to undertake the information management function</div>
    <div class="check" style="top:48px"><svg width="3" height="3" viewBox="0 0 3 3"><path d="M.3 1.5L1.2 2.5 2.8.3"/></svg>Appointment level</div>
    <div class="check" style="top:53px"><svg width="3" height="3" viewBox="0 0 3 3"><path d="M.3 1.5L1.2 2.5 2.8.3"/></svg>Information Procurement Stage</div>
    <div class="check" style="top:58px"><svg width="3" height="3" viewBox="0 0 3 3"><path d="M.3 1.5L1.2 2.5 2.8.3"/></svg>Actor: The Lead Appointed Party</div>
    <div class="video" role="img" aria-label="Video still of engineers reviewing plans on site"><div class="playc"></div></div>
    <svg class="player" width="49" height="9" viewBox="0 0 49 9"><path fill="#fff" d="M12 4.5l3-2v4zM15 4.5l3-2v4zM23 2.5l4 2-4 2zM31 2.5l3 2-3 2zM34 2.5l3 2-3 2z"/></svg>
    <div class="slider"><span></span></div>
    <div class="cap">Illustration</div>
    <div class="lorem">Lorem ipsum is sometimes known as dummy text used in laying out print.</div>
  </div>
</section>

<section class="set t3">
  <div class="screen s1">
    <div class="header" style="height:44px"></div>
    <svg class="wave" style="top:43px" width="75" height="12" viewBox="0 0 75 12" preserveAspectRatio="none"><path d="M0 0H75V2C60 2 52 12 35 10S10 3 0 10Z"/></svg>
    <div class="status light">22:14</div>
    <div class="head-text" style="top:22px">Welcome to<br>Virtual Engineering Leaders</div>
    <div class="brand">Velmiro</div>
    <div class="field" style="top:82px">Email</div>
    <div class="field" style="top:94px">Password</div>
    <div class="btn" style="top:109px">Login</div>
    <div class="small" style="top:124px">Sign up &nbsp;OR&nbsp; Sign up via <b>Crewnet</b></div>
    <div class="skyline" role="img" aria-label="Construction site skyline illustration"></div>
  </div>
  <div class="screen s2">
    <div class="status">22:14</div>
    <div class="title" style="top:21px">Create an Account</div>
    <div class="field" style="top:35px">Name</div>
    <div class="field" style="top:47px">Email</div>
    <div class="field" style="top:59px">Mobile No.</div>
    <div class="field" style="top:71px">Password</div>
    <div class="field" style="top:83px">Gender</div>
    <div class="field" style="top:95px">Country of Residence</div>
    <div class="field" style="top:107px">Company</div>
    <div class="field" style="top:119px">Title</div>
    <div class="field" style="top:131px">Year of Experience</div>
    <div class="btn" style="top:146px;background:var(--btn2)">Sign Up</div>
  </div>
  <div class="screen s3">
    <div class="status">22:14</div>
    <div class="title" style="top:21px">Your Journey Starts Here</div>
    <div class="bar cust" style="top:33px">Customise your Journey</div>
    <div class="opts">
      <div class="opt" style="top:3px">Show All</div>
      <div class="opt" style="top:8px">I am the client (Appointing Party)</div>
      <div class="opt" style="top:14px">I am the lead consultant / lead contractor (Appointed Party)</div>
      <div class="opt" style="top:25px">I am the consultant / subcontractor / supplier (Appointed Party)</div>
    </div>
    <div class="bar list" style="top:86px">How to start BIM?</div>
    <div class="bar list" style="top:95px">Important ISO19650 principles to know</div>
    <div class="bar list" style="top:104px">Information Management Processes &amp; Act…</div>
    <div class="bar list" style="top:113px">Documents/Resources You Need to Develop</div>
    <div class="bar list" style="top:122px">Other Resources</div>
    <div class="skyline" role="img" aria-label="Crane and building site illustration"></div>
  </div>
  <div class="screen s4">
    <div class="side-status">▮▮</div>
    <div class="menu">
      <div class="avatar" role="img" aria-label="Profile photo of the user"></div>
      <div class="name">Name Here</div>
      <div class="role">Professionals</div>
      <div class="item fav" style="top:51px"><i></i>My favorite</div>
      <div class="item" style="top:62px"><i></i>Search</div>
      <div class="item" style="top:73px"><i></i>About the app</div>
      <div class="item" style="top:84px"><i></i>About the authors</div>
      <div class="item" style="top:95px"><i></i>Log out</div>
      <div class="skyline" role="img" aria-label="Workers and crane on a building site illustration"></div>
    </div>
  </div>
  <div class="screen s5">
    <div class="header" style="height:30px"></div>
    <svg class="wave" style="top:29px" width="75" height="12" viewBox="0 0 75 12" preserveAspectRatio="none"><path d="M0 0H75V4C60 12 40 2 20 8S5 9 0 6Z"/></svg>
    <div class="status light">22:14</div>
    <div class="head-text" style="top:13px">Nominate individuals to undertake the information management function</div>
    <div class="check" style="top:48px"><svg width="3" height="3" viewBox="0 0 3 3"><path d="M.3 1.5L1.2 2.5 2.8.3"/></svg>Appointment level</div>
    <div class="check" style="top:53px"><svg width="3" height="3" viewBox="0 0 3 3"><path d="M.3 1.5L1.2 2.5 2.8.3"/></svg>Information Procurement Stage</div>
    <div class="check" style="top:58px"><svg width="3" height="3" viewBox="0 0 3 3"><path d="M.3 1.5L1.2 2.5 2.8.3"/></svg>Actor: The Lead Appointed Party</div>
    <div class="video" role="img" aria-label="Video still of engineers reviewing plans on site"><div class="playc"></div></div>
    <svg class="player" width="49" height="9" viewBox="0 0 49 9"><path fill="#fff" d="M12 4.5l3-2v4zM15 4.5l3-2v4zM23 2.5l4 2-4 2zM31 2.5l3 2-3 2zM34 2.5l3 2-3 2z"/></svg>
    <div class="slider"><span></span></div>
    <div class="cap">Illustration</div>
    <div class="lorem">Lorem ipsum is sometimes known as dummy text used in laying out print.</div>
  </div>
</section>

<section class="set t4">
  <div class="screen s1">
    <div class="header" style="height:44px"></div>
    <svg class="wave" style="top:43px" width="75" height="12" viewBox="0 0 75 12" preserveAspectRatio="none"><path d="M0 0H75V2C60 2 52 12 35 10S10 3 0 10Z"/></svg>
    <div class="status light">22:14</div>
    <div class="head-text" style="top:22px">Welcome to<br>Virtual Engineering Leaders</div>
    <div class="brand">Velmiro</div>
    <div class="field" style="top:82px">Email</div>
    <div class="field" style="top:94px">Password</div>
    <div class="btn" style="top:109px">Login</div>
    <div class="small" style="top:124px">Sign up &nbsp;OR&nbsp; Sign up via <b>Crewnet</b></div>
    <div class="skyline" role="img" aria-label="Construction site skyline illustration"></div>
  </div>
  <div class="screen s2">
    <div class="status">22:14</div>
    <div class="title" style="top:21px">Create an Account</div>
    <div class="field" style="top:35px">Name</div>
    <div class="field" style="top:47px">Email</div>
    <div class="field" style="top:59px">Mobile No.</div>
    <div class="field" style="top:71px">Password</div>
    <div class="field" style="top:83px">Gender</div>
    <div class="field" style="top:95px">Country of Residence</div>
    <div class="field" style="top:107px">Company</div>
    <div class="field" style="top:119px">Title</div>
    <div class="field" style="top:131px">Year of Experience</div>
    <div class="btn" style="top:146px;background:var(--btn2)">Sign Up</div>
  </div>
  <div class="screen s3">
    <div class="status">22:14</div>
    <div class="title" style="top:21px">Your Journey Starts Here</div>
    <div class="bar cust" style="top:33px">Customise your Journey</div>
    <div class="opts">
      <div class="opt" style="top:3px">Show All</div>
      <div class="opt" style="top:8px">I am the client (Appointing Party)</div>
      <div class="opt" style="top:14px">I am the lead consultant / lead contractor (Appointed Party)</div>
      <div class="opt" style="top:25px">I am the consultant / subcontractor / supplier (Appointed Party)</div>
    </div>
    <div class="bar list" style="top:86px">How to start BIM?</div>
    <div class="bar list" style="top:95px">Important ISO19650 principles to know</div>
    <div class="bar list" style="top:104px">Information Management Processes &amp; Act…</div>
    <div class="bar list" style="top:113px">Documents/Resources You Need to Develop</div>
    <div class="bar list" style="top:122px">Other Resources</div>
    <div class="skyline" role="img" aria-label="Crane and building site illustration"></div>
  </div>
  <div class="screen s4">
    <div class="side-status">▮▮</div>
    <div class="menu">
      <div class="avatar" role="img" aria-label="Profile photo of the user"></div>
      <div class="name">Name Here</div>
      <div class="role">Professionals</div>
      <div class="item fav" style="top:51px"><i></i>My favorite</div>
      <div class="item" style="top:62px"><i></i>Search</div>
      <div class="item" style="top:73px"><i></i>About the app</div>
      <div class="item" style="top:84px"><i></i>About the authors</div>
      <div class="item" style="top:95px"><i></i>Log out</div>
      <div class="skyline" role="img" aria-label="Workers and crane on a building site illustration"></div>
    </div>
  </div>
  <div class="screen s5">
    <div class="header" style="height:30px"></div>
    <svg class="wave" style="top:29px" width="75" height="12" viewBox="0 0 75 12" preserveAspectRatio="none"><path d="M0 0H75V4C60 12 40 2 20 8S5 9 0 6Z"/></svg>
    <div class="status light">22:14</div>
    <div class="head-text" style="top:13px">Nominate individuals to undertake the information management function</div>
    <div class="check" style="top:48px"><svg width="3" height="3" viewBox="0 0 3 3"><path d="M.3 1.5L1.2 2.5 2.8.3"/></svg>Appointment level</div>
    <div class="check" style="top:53px"><svg width="3" height="3" viewBox="0 0 3 3"><path d="M.3 1.5L1.2 2.5 2.8.3"/></svg>Information Procurement Stage</div>
    <div class="check" style="top:58px"><svg width="3" height="3" viewBox="0 0 3 3"><path d="M.3 1.5L1.2 2.5 2.8.3"/></svg>Actor: The Lead Appointed Party</div>
    <div class="video" role="img" aria-label="Video still of engineers reviewing plans on site"><div class="playc"></div></div>
    <svg class="player" width="49" height="9" viewBox="0 0 49 9"><path fill="#fff" d="M12 4.5l3-2v4zM15 4.5l3-2v4zM23 2.5l4 2-4 2zM31 2.5l3 2-3 2zM34 2.5l3 2-3 2z"/></svg>
    <div class="slider"><span></span></div>
    <div class="cap">Illustration</div>
    <div class="lorem">Lorem ipsum is sometimes known as dummy text used in laying out print.</div>
  </div>
</section>

</body>
</html>
```